Lanternleaf take out menu

We need a take out menu design using our menu attached. Info to include would be our address: 7816 Brindlewood Hollow Pkwy #204, Lafayette, LA 70508. Phone number is 337-514-2960. website is www.lanternleafgrv.com.

Industry/Entity Type

Asian Restaurant

```html
<!DOCTYPE html>
<html lang="en">
<head>
<meta charset="utf-8">
<title>Lanternleaf Take Out Menu</title>
<link href="https://fonts.googleapis.com/css2?family=Ranchers&family=Noto+Sans:wght@400;700&family=Arimo:wght@400;700&display=swap" rel="stylesheet">
<style>
  :root {
    --canvas: #efe9df;
    --paper: #ffffff;
    --menu-red: #d92128;
    --frame-lime: #d3df1f;
    --ink: #1a1a1a;
    --shadow: rgba(0,0,0,0.18);
  }
  * { box-sizing: border-box; margin: 0; padding: 0; }
  html, body { width: 1200px; height: 1200px; overflow: hidden; }
  body { background: var(--canvas); position: relative; font-family: "Noto Sans", sans-serif; color: var(--ink); }

  .page {
    position: absolute; width: 391px; height: 554px;
    background: var(--paper); box-shadow: 0 2px 6px var(--shadow); overflow: hidden;
  }
  .page--cover { left: 197px; top: 26px; background: var(--menu-red); }
  .page--story { left: 615px; top: 26px; }
  .page--starters-a { left: 197px; top: 601px; }
  .page--starters-b { left: 615px; top: 601px; }

  .frame { position: absolute; inset: 0; width: 100%; height: 100%; }
  .frame path, .frame rect { fill: none; stroke: var(--frame-lime); stroke-width: 2.4; }

  .brand-tab {
    position: absolute; left: 138px; width: 113px; background: var(--paper);
    display: flex; flex-direction: column; align-items: center; justify-content: center; gap: 5px;
  }
  .brand-tab--top { top: 0; height: 126px; border-radius: 0 0 56px 56px; padding-top: 8px; }
  .brand-tab--bottom { bottom: 0; height: 132px; border-radius: 56px 56px 0 0; padding-top: 4px; }
  .brand-dot { width: 34px; height: 34px; border-radius: 50%; background: var(--menu-red); }
  .brand-name { font-family: "Noto Sans", sans-serif; font-weight: 700; font-size: 14px; color: var(--menu-red); letter-spacing: 0.5px; }

  .cover-title {
    position: absolute; left: 0; right: 0; top: 245px; text-align: center;
    font-family: "Ranchers", sans-serif; font-size: 66px; color: var(--frame-lime); letter-spacing: 2px;
  }

  .section-title {
    position: absolute; left: 0; right: 0; text-align: center;
    font-family: "Ranchers", sans-serif; font-weight: 400; color: var(--menu-red); letter-spacing: 1px;
  }
  .page--story .section-title { top: 76px; font-size: 21px; }
  .page--starters-a .section-title, .page--starters-b .section-title { top: 45px; font-size: 19px; }

  .story-text { position: absolute; left: 73px; top: 164px; width: 270px; font-size: 9.2px; line-height: 11.2px; white-space: nowrap; }
  .story-text p + p { margin-top: 11.2px; }

  .contact {
    position: absolute; left: 60px; right: 60px; top: 462px; text-align: center;
    font-size: 8.8px; line-height: 12.5px; color: var(--ink);
  }
  .contact__phone, .contact__web { color: var(--menu-red); font-weight: 700; }

  .dish-list { position: absolute; list-style: none; display: flex; flex-direction: column; justify-content: space-between; }
  .dish-head { display: flex; justify-content: space-between; font-weight: 700; }
  .dish-price { font-weight: 400; }
  .dish-desc { white-space: nowrap; }

  .page--starters-a .dish-list { left: 65px; width: 256px; top: 82px; height: 394px; }
  .page--starters-a .dish-head { font-size: 11.2px; line-height: 13px; }
  .page--starters-a .dish-desc { font-size: 9.3px; line-height: 12px; }

  .page--starters-b .dish-list { font-family: "Arimo", sans-serif; left: 66px; width: 258px; top: 86px; height: 394px; }
  .page--starters-b .dish-head { font-size: 11.2px; line-height: 13px; }
  .page--starters-b .dish-desc { font-size: 8.6px; line-height: 13px; }
</style>
</head>
<body>

<section class="page page--cover">
  <svg class="frame" viewBox="0 0 391 554" aria-hidden="true">
    <path d="M130,26 H26 V528 H130 M261,26 H365 V528 H261 M130,32 H32 V522 H130 M261,32 H359 V522 H261"/>
    <rect x="20" y="20" width="14" height="14"/><rect x="357" y="20" width="14" height="14"/>
    <rect x="20" y="520" width="14" height="14"/><rect x="357" y="520" width="14" height="14"/>
  </svg>
  <div class="brand-tab brand-tab--top"><span class="brand-dot"></span><span class="brand-name">Lanternleaf</span></div>
  <h1 class="cover-title">MENU</h1>
  <div class="brand-tab brand-tab--bottom"><span class="brand-dot"></span><span class="brand-name">Lanternleaf</span></div>
</section>

<section class="page page--story">
  <svg class="frame" viewBox="0 0 391 554" aria-hidden="true">
    <path d="M130,26 H26 V528 H130 M261,26 H365 V528 H261 M130,32 H32 V522 H130 M261,32 H359 V522 H261"/>
    <rect x="20" y="20" width="14" height="14"/><rect x="357" y="20" width="14" height="14"/>
    <rect x="20" y="520" width="14" height="14"/><rect x="357" y="520" width="14" height="14"/>
  </svg>
  <h2 class="section-title">OUR STORY</h2>
  <div class="story-text">
    <p>At Lanternleaf, we pride ourselves in serving fresh,<br>authentic Sichuan Chinese cuisine delicately<br>prepared by our expertly trained Chefs.</p>
    <p>Sichuan cuisine originates from southwest China<br>between the Sichuan Basin and Tibetan Plateau.<br>It is known for being both very spicy and flavorful,<br>much like our own southern Louisiana cuisine.</p>
    <p>Our Executive Chef, Meilin Zhao grew up in the<br>southwestern Chinese province of Sichuan, China<br>where he began his training at fifteen years old<br>under his grandfather’s mentorship. Chef Zhao<br>became an acclaimed chef in his province, opening<br>several restaurants and traveling throughout China<br>to cater for many of China’s elite. His dream was to<br>share his Sichuan style with the world which lead<br>him to the United States. He has worked in<br>restaurants in both Houston and New York and we<br>now welcome him to his new home in Lafayette,<br>Louisiana.</p>
    <p>We are very excited to bring to Lafayette the<br>authenticity of Chinese cuisine and hope you enjoy<br>your experience dining with us.</p>
  </div>
  <address class="contact">
    7816 Brindlewood Hollow Pkwy #204, Lafayette, LA 70508<br>
    <span class="contact__phone">337-514-2960</span> &nbsp;|&nbsp; <span class="contact__web">www.lanternleafgrv.com</span>
  </address>
</section>

<section class="page page--starters-a">
  <svg class="frame" viewBox="0 0 391 554" aria-hidden="true">
    <path d="M130,26 H26 V528 H130 M261,26 H365 V528 H261 M130,32 H32 V522 H130 M261,32 H359 V522 H261"/>
    <rect x="20" y="20" width="14" height="14"/><rect x="357" y="20" width="14" height="14"/>
    <rect x="20" y="520" width="14" height="14"/><rect x="357" y="520" width="14" height="14"/>
  </svg>
  <h2 class="section-title">APPETIZERS</h2>
  <ul class="dish-list">
    <li><div class="dish-head"><span>Edamame</span><span class="dish-price">$4</span></div><p class="dish-desc">Seasoned &amp; boiled soy bean</p></li>
    <li><div class="dish-head"><span>Scallion Pancakes</span><span class="dish-price">$6</span></div><p class="dish-desc">Traditional Chinese flatbread folded<br>with oil and minced scallions and pan fried</p></li>
    <li><div class="dish-head"><span>Lanternleaf Lettuce Wraps</span><span class="dish-price">$8</span></div><p class="dish-desc">Seasoned ground chicken drizzled with our top secret<br>homemade sauce served with lettuce wraps</p></li>
    <li><div class="dish-head"><span>Salt &amp; Pepper Calamari</span><span class="dish-price">$9</span></div><p class="dish-desc">Crispy Calamari with Green &amp; red peppers and onions</p></li>
    <li><div class="dish-head"><span>Buddha Bang Shrimp</span><span class="dish-price">$9</span></div><p class="dish-desc">Crispy fried shrimp tossed in our creamy spicy sauce</p></li>
    <li><div class="dish-head"><span>Drunken Chicken</span><span class="dish-price">$8</span></div><p class="dish-desc">Chicken, Thai chili in a house made spicy sauce</p></li>
    <li><div class="dish-head"><span>Sichuan Spiced Beef</span><span class="dish-price">$9</span></div><p class="dish-desc">Beef Shank, beef tripe, cilantro, peanuts and celery</p></li>
    <li><div class="dish-head"><span>Beef Crispy Bottom Bao</span><span class="dish-price">$10</span></div><p class="dish-desc">Pan fried crispy bottom Bao, stuffed with beef,<br>drizzled with scallion and sesame (Fresh made to<br>order, takes at least 20 mins to serve)</p></li>
    <li><div class="dish-head"><span>Shrimp &amp; Beef Crispy Bottom Bao</span><span class="dish-price">$10</span></div><p class="dish-desc">Pan fried crispy bottom Bao, stuffed with<br>beef and shrimp, drizzled with scallion and sesame<br>(Fresh made to order, takes at least 20 mins to serve)</p></li>
  </ul>
</section>

<section class="page page--starters-b">
  <svg class="frame" viewBox="0 0 391 554" aria-hidden="true">
    <path d="M130,26 H26 V528 H130 M261,26 H365 V528 H261 M130,32 H32 V522 H130 M261,32 H359 V522 H261"/>
    <rect x="20" y="20" width="14" height="14"/><rect x="357" y="20" width="14" height="14"/>
    <rect x="20" y="520" width="14" height="14"/><rect x="357" y="520" width="14" height="14"/>
  </svg>
  <h2 class="section-title">APPETIZERS</h2>
  <ul class="dish-list">
    <li><div class="dish-head"><span>Crispy Mala Beef Jerky</span><span class="dish-price">$9</span></div><p class="dish-desc">Dry fried shredded beef with various peppers in sesame<br>and peppercorn oil</p></li>
    <li><div class="dish-head"><span>Fried Chicken Dumplings (6)</span><span class="dish-price">$6</span></div><p class="dish-desc">Chinese dumpling stuffed with Chicken,<br>Shiitake mushrooms and bamboo shoots</p></li>
    <li><div class="dish-head"><span>Red Oil Dumplings (6)</span><span class="dish-price">$7</span></div><p class="dish-desc">Pork filled dumplings in Sichuan red oil sauce drizzled<br>with sesame</p></li>
    <li><div class="dish-head"><span>Pork Egg Rolls (2)</span><span class="dish-price">$4</span></div><p class="dish-desc">Hand rolled with julienned veggies with<br>our sweet n’ sour mustard sauce</p></li>
    <li><div class="dish-head"><span>Vegetarian Spring Rolls (3)</span><span class="dish-price">$4</span></div><p class="dish-desc">Traditional Asian Roll served with a sweet chili sauce</p></li>
    <li><div class="dish-head"><span>Garlic Cucumber Salad</span><span class="dish-price">$7</span></div><p class="dish-desc">Sliced cucumber with a garlic vinaigrette</p></li>
    <li><div class="dish-head"><span>Hot n’ Sour Soup</span><span class="dish-price">$4</span></div><p class="dish-desc">Tangy broth with Bamboo shoot, wood ear fungus,<br>tofu, egg and carrots</p></li>
    <li><div class="dish-head"><span>West Lake Soup</span><span class="dish-price">$4</span></div><p class="dish-desc">Light creamy soup with ground beef,<br>diced Shiitake mushroom, tofu, bamboo shoots,<br>egg white and cilantro</p></li>
  </ul>
</section>

</body>
</html>
```